Business Card Design

Our Pharmacy Opens late - the last to close in Brisbane
over 30 years since opened.
Open from 7am - 11pm every day.
Next to Corbrook 7 Day Medical Centre
Parking in front of shop
Sit with a pharmacist for every script - the best advice every time.
Private consulting room.
We have the medication that you need.
Wide range Home Health Care products.

Looking for a card that my (young) staff feel happy to hand out to people they they meet.
Updates

Hello Many thanks for your submissions I just need to clarify the costings for this project as per my updated brief Please confirm then we can proceed Many thanks Desmond

Reason: due to the adjusted brief and query I have extended the deadline Many thanks for those that have submitted, I will choose the designer as soon as I understand the costings of the project, as per the message despatched today Regards desmond

Target Market(s)

men and women 30-70

Industry/Entity Type

Business

Contact Information for Business Card

Pelworth Pharmacy - Corbrook
317 Tolland Rd
Corbrook 4186
Last to Close
Open 7am - 11pm

Font styles to use
Sans Serif

Requirements
Must have
• each batch of 250 will have the following staff names

Lorraine Muskett, Senior Pharmacist
Fatima Oduya, Pharmacist
Bo Lam, Pharmacist
Ondine Whitlaw, Pharmacist
Greta Volm, Retail Manager
Tess Ruvolo, Marketing Manager
Desmond Pelworth, Pharmacist Proprietor
Should not have
• Please advise if the cost of this job covers the 7 individualised business cards.

Each staff member needs their own card.

please advise

```html
<!DOCTYPE html>
<html lang="en">
<head>
<meta charset="utf-8">
<title>Pelworth Pharmacy – Business Card</title>
<link rel="stylesheet" href="https://fonts.googleapis.com/css2?family=Arimo:ital,wght@0,400;0,700;1,700&display=swap">
<style>
  :root {
    --navy: #1f2d5c;
    --yellow: #f3e620;
    --white: #ffffff;
    --backdrop: #e7e8ec;
    --ink: #111111;
  }
  * { box-sizing: border-box; margin: 0; padding: 0; }
  html, body { width: 1200px; height: 523px; overflow: hidden; }
  body {
    background: var(--backdrop);
    font-family: "Arimo", Arial, sans-serif;
    display: flex;
    align-items: center;
    justify-content: center;
  }
  .business-card {
    width: 860px;
    height: 469px;
    background: var(--white);
    display: grid;
    grid-template-rows: 140px 1fr 88px;
    box-shadow: 0 6px 18px rgba(0,0,0,0.18);
  }
  .card-header {
    background: var(--navy);
    position: relative;
    padding: 40px 0 0 34px;
  }
  .staff-name {
    color: var(--yellow);
    font-weight: 700;
    font-size: 44px;
    letter-spacing: 0.5px;
    line-height: 1;
    text-transform: uppercase;
  }
  .staff-role {
    color: var(--white);
    font-weight: 700;
    font-style: italic;
    font-size: 22px;
    margin-top: 4px;
    margin-left: 6px;
  }
  .brand-mark-small {
    position: absolute;
    top: 30px;
    right: 30px;
    display: flex;
    align-items: center;
    gap: 10px;
  }
  .brand-mark-small .brand-dot { width: 26px; height: 26px; }
  .brand-mark-small .brand-name {
    color: var(--white);
    font-weight: 700;
    font-size: 20px;
  }
  .card-body {
    display: flex;
    align-items: center;
    padding: 0 40px 0 54px;
  }
  .brand-mark-large {
    display: flex;
    align-items: center;
    gap: 16px;
    width: 380px;
  }
  .brand-mark-large .brand-dot { width: 56px; height: 56px; flex: none; }
  .brand-mark-large .brand-name {
    color: var(--navy);
    font-weight: 700;
    font-size: 34px;
    line-height: 1.1;
  }
  .divider {
    width: 5px;
    height: 160px;
    background: var(--navy);
    margin: 0 20px 0 24px;
  }
  .contact-list {
    list-style: none;
    color: var(--navy);
    font-weight: 700;
    font-size: 26px;
    line-height: 1.35;
  }
  .card-footer {
    background: var(--yellow);
    display: flex;
    align-items: center;
    justify-content: center;
  }
  .address {
    color: var(--ink);
    font-weight: 700;
    font-size: 26px;
  }
</style>
</head>
<body>
  <article class="business-card">
    <header class="card-header">
      <h1 class="staff-name">Lorraine Muskett</h1>
      <p class="staff-role">Senior Pharmacist</p>
      <div class="brand-mark-small">
        <svg class="brand-dot" viewBox="0 0 26 26" aria-hidden="true"><circle cx="13" cy="13" r="13" fill="#f3e620"/></svg>
        <span class="brand-name">Pelworth Pharmacy</span>
      </div>
    </header>
    <section class="card-body">
      <div class="brand-mark-large">
        <svg class="brand-dot" viewBox="0 0 56 56" aria-hidden="true"><circle cx="28" cy="28" r="28" fill="#f3e620"/></svg>
        <span class="brand-name">Pelworth Pharmacy</span>
      </div>
      <div class="divider"></div>
      <ul class="contact-list">
        <li>OPEN: 7am - 11pm</li>
        <li>Phone: 555-0148</li>
        <li>Email:</li>
      </ul>
    </section>
    <footer class="card-footer">
      <p class="address">Corbrook 317 Tolland Rd Corbrook 4186</p>
    </footer>
  </article>
</body>
</html>
```